Antibacterial Hand Wash Squeeze Tube Label

We're looking for a contemporary label design for a new Antibacterial Hand Wash for an 8oz squeeze tube. The new consumer brand will be sold to consumers in major US retail stores & online. The moisturizing hand wash contains Aloe Vera, vitamin E, and other natural ingredients so the design should include the color green. Real photos are very effective on packaging, so a picture of Aloe Vera or possibly two hands washing would help draw consumers' attention to the tube on the retail shelf. The front label may wrap around the sides. Rear must be left mostly blank
Target Market(s)
US Consumers - retail stores & online
Industry/Entity Type
Consumer

```html
<!DOCTYPE html>
<html lang="en">
<head>
<meta charset="utf-8">
<title>Antibacterial Hand Wash – Tube Label</title>
<link href="https://fonts.googleapis.com/css2?family=Chewy&family=Patrick+Hand&display=swap" rel="stylesheet">
<style>
  :root {
    --page-bg: #ffffff;
    --label-light: #f7f7f7;
    --label-edge: #dcdcdc;
    --leaf-green: #5cc22a;
    --leaf-dark: #3f9a17;
    --aqua: #1ec3f0;
    --alert-red: #ee1f2b;
    --skin: #e9cfc4;
    --band-white: #fbf8f6;
  }
  html, body {
    margin: 0;
    width: 1200px;
    height: 1200px;
    overflow: hidden;
    background: var(--page-bg);
  }
  .label {
    position: absolute;
    left: 384px;
    top: 100px;
    width: 432px;
    height: 1000px;
    background: linear-gradient(90deg, var(--label-edge) 0%, var(--label-light) 30%, var(--label-light) 60%, var(--label-edge) 100%);
    overflow: hidden;
    font-family: "Chewy", "Patrick Hand", sans-serif;
  }
  .brand {
    position: absolute;
    left: 0;
    top: 70px;
    width: 100%;
    display: flex;
    justify-content: center;
    align-items: center;
    gap: 8px;
    color: var(--leaf-green);
    font-size: 24px;
    line-height: 1;
  }
  .brand-dot {
    width: 12px;
    height: 12px;
    border-radius: 50%;
    background: var(--leaf-green);
  }
  .title {
    position: absolute;
    left: 0;
    width: 100%;
    text-align: center;
    margin: 0;
    font-weight: 400;
    line-height: 1;
    font-size: 124px;
    -webkit-text-stroke: 2px #ffffff;
  }
  .title-hand { top: 112px; color: var(--leaf-green); }
  .title-wash { top: 240px; color: var(--aqua); padding-left: 24px; box-sizing: border-box; }
  .aloe-photo {
    position: absolute;
    left: 36px;
    top: 372px;
    width: 396px;
    height: 234px;
    background: radial-gradient(ellipse at 35% 60%, #d9f0c8 0%, #8fd65a 40%, var(--leaf-green) 70%, rgba(92,194,42,0) 100%);
  }
  .claims {
    position: absolute;
    left: 0;
    top: 606px;
    width: 100%;
    height: 262px;
    background: var(--band-white);
    text-align: center;
  }
  .claim-main {
    margin: 10px 0 2px;
    font-size: 54px;
    color: var(--alert-red);
    font-weight: 400;
    line-height: 1.05;
  }
  .benefits {
    list-style: none;
    margin: 0;
    padding: 0;
    font-family: "Patrick Hand", sans-serif;
    font-weight: 700;
    line-height: 1.08;
  }
  .benefits li { font-size: 46px; }
  .benefits li::before { content: "• "; font-size: 26px; vertical-align: middle; }
  .benefit-aqua { color: var(--aqua); }
  .benefit-green { color: var(--leaf-dark); }
  .benefits .benefit-small { font-size: 24px; padding-right: 24px; }
  .benefits .benefit-small::before { font-size: 16px; }
  .hands-photo {
    position: absolute;
    left: 0;
    top: 868px;
    width: 100%;
    height: 132px;
    background: linear-gradient(180deg, var(--band-white) 0%, var(--skin) 45%, #f3e4dc 100%);
  }
</style>
</head>
<body>
  <main class="label">
    <div class="brand"><span class="brand-dot"></span><span class="brand-name">VERDANEL</span></div>
    <h1 class="title title-hand">Hand</h1>
    <h1 class="title title-wash">Wash</h1>
    <div class="aloe-photo" role="img" aria-label="Photo of freshly sliced aloe vera leaves"></div>
    <section class="claims">
      <p class="claim-main">Antibacterial</p>
      <ul class="benefits">
        <li class="benefit-aqua">Moisturizing</li>
        <li class="benefit-green">Aloe Vera</li>
        <li class="benefit-aqua">Vitamin E</li>
        <li class="benefit-green benefit-small">Other natural ingredients</li>
      </ul>
    </section>
    <div class="hands-photo" role="img" aria-label="Photo of two hands being washed with lather"></div>
  </main>
</body>
</html>
```